Market place for used airplanes/helicopters/parts

http://www.vingtorget.se needs a facelift.

# What is it
Classifieds for used airplanes/helicopters/parts/spare parts/aviation literature, for people in Scandinavia. The number of classifieds is ~120-200. They are mainly in Swedish, English, Norwegian.

It's not a glamorous or luxurious business, but more for people with a genuine interest in flying, technical things.

Similar to sites like this, but they have much more classifieds than my site
http://www.skyquarry.com/list/list.aspx?ETID=1&setype=1&catid=6
http://www.lindqvistflyg.com/planes.asp?meny=1&typ=single
https://www.propwashdeals.com/cat.php?mode=listing&main=

# What I want
Design only - no code. I want a modern, maybe a bit bootstrap like, clean, simple, not flashy, web design. I want the design to be in English.

# Audience of the website
Aviation interested men, 45-65 years old, in the nordic countries (around Sweden).

# Logotype that could be used (but not necessarily)
http://www.vingtorget.se/flygplan_till_salu_large.jpg
http://www.vingtorget.se/flygplan_till_salu.eps

Reason: I decided to extend the deadline with 1 day. The reason is that I (unfortunately) managed to put the contest in the wrong category for 1 day + I want to give you all feedback (been too busy the whole day, sorry).

Hi all! 

Thanks everyone for the contributions you made. 

I will setup a poll for the designs that I like most. Will get back when I have more information. 

Thanks and have a nice weekend!
Kjell

Target Market(s)

45-65 old Scandinavian men

Industry/Entity Type

Business

Requirements
Must have
• - A list with classifieds on the first page, so the visitor easily can see new classifieds.
- A classifieds should be able to have more than one photo
- A simple navigation for showing classifieds from categories like airplanes, helicopters/gyrocopters, parts, literature, misc (maybe other categories) .... but still, it's just 100-200 ads so it's not needed that much filtration.

- A placeholder/way of showing aviation news/clips. In the old design I had, it was a column to the right. It's enough to show maybe 2-5 placeholders.
- A placeholder for PlaceAds ads somewhere on the site.
Should not have
• - Carousels
- Too much clutter

```html
<!DOCTYPE html>
<html lang="en">
<head>
<meta charset="utf-8">
<title>Vingtorget – Aircraft For Sale</title>
<link href="https://fonts.googleapis.com/css2?family=Lato:wght@300;400;700;900&display=swap" rel="stylesheet">
<style>
:root{
  --blue:#0a5aa8;
  --blue-bright:#1a8be0;
  --sky-top:#bcd8ef;
  --sky-bottom:#f3f8fc;
  --navy:#2f4259;
  --page:#e9e9e9;
  --white:#ffffff;
  --text:#6a6a6a;
  --dark:#333;
  --line:#dcdcdc;
  --red:#d23a2a;
}
*{box-sizing:border-box;margin:0;padding:0}
html,body{width:869px;height:1200px;overflow:hidden}
body{position:relative;background:var(--page);font-family:'Lato',sans-serif;color:var(--text)}
.header{position:absolute;left:0;top:0;width:869px;height:108px;background:linear-gradient(180deg,var(--sky-top),var(--sky-bottom))}
.brand{position:absolute;left:0;width:869px;top:24px;text-align:center;font-weight:900;font-size:22px;color:var(--blue);letter-spacing:-.5px}
.brand-name{font-weight:900}
.social{position:absolute;right:146px;top:86px;display:flex;gap:5px}
.social span{width:16px;height:16px;border-radius:50%;background:var(--white);border:1px solid #cfe0ee}
.nav{position:absolute;top:108px;left:0;width:869px;height:36px;background:var(--blue);border-top:2px solid #2f8fdc}
.nav ul{list-style:none;display:flex;position:absolute;left:138px;top:0;height:34px}
.nav li{color:var(--white);font-size:11.5px;padding:0 7px;line-height:34px;border-right:1px solid #0b4e8f;letter-spacing:-.3px}
.nav li:last-child{border:0}
.search{position:absolute;left:480px;top:6px;width:239px;height:24px;background:var(--white);font-size:7px;color:#aaa;line-height:24px;padding-left:15px}
.search-btn{position:absolute;left:689px;top:6px;width:30px;height:24px;background:var(--blue-bright)}
.search-btn svg{position:absolute;left:8px;top:5px}
.page-title{position:absolute;left:144px;top:166px;font-size:25px;font-weight:700;color:var(--blue);letter-spacing:-1px}
.welcome{position:absolute;left:145px;top:200px;font-size:10.5px;color:var(--dark);letter-spacing:-.3px}
.welcome a{color:var(--blue-bright);text-decoration:none;font-weight:700}
.rule{position:absolute;left:144px;top:229px;width:575px;height:1px;background:#cfcfcf}
.card{position:absolute;left:144px;width:408px;background:var(--white)}
.card-head{height:32px;background:var(--navy);color:var(--white);font-size:18px;font-weight:700;padding-left:19px;line-height:32px;letter-spacing:-.8px}
.thumbs{display:flex;gap:1px;padding:10px 0 0 18px}
.thumbs div{width:69px;height:56px}
.desc{font-size:7.5px;line-height:11px;padding:8px 18px 0;letter-spacing:-.1px}
.desc p+p{margin-top:5px}
.more{color:var(--blue);font-weight:700;margin-left:4px}
.side-photo{display:flex;padding:10px 18px 0;gap:10px}
.side-photo .desc{padding:0}
.side-photo .thumb{flex:none;width:68px;height:66px;margin-top:12px}
.meta{display:flex;gap:10px;margin-top:6px;border-top:1px solid var(--line);border-bottom:1px solid var(--line);height:26px;align-items:center;padding-left:18px;font-size:7.5px;font-weight:700;color:var(--dark)}
.meta b{color:var(--blue)}
.meta svg{vertical-align:-2px;margin-right:3px}
.dated{display:flex;align-items:center;height:24px;padding:0 15px 0 18px;font-size:7.5px;font-weight:700;color:var(--blue)}
.dated .dots{flex:1;border-top:1px dotted #bbb;margin:0 12px 0 16px}
.btn{background:var(--blue);color:var(--white);font-size:6px;padding:4px 5px;border-radius:1px}
.box-head{height:26px;background:var(--blue);color:var(--white);font-size:11px;font-weight:700;line-height:26px;padding-left:11px;letter-spacing:-.4px}
.side{position:absolute;left:565px;width:153px}
.video{top:248px}
.video-frame{height:101px;background:var(--white);padding:2px}
.video-frame div{height:97px;background:linear-gradient(135deg,#555,#222 60%,#444);position:relative}
.news{top:388px;background:var(--white)}
.news-item{display:flex;gap:10px;padding:8px 6px 7px 11px;border-bottom:1px solid var(--line);height:55px}
.news-item:last-child{border:0}
.day{text-align:center;width:30px;color:var(--dark)}
.day b{display:block;width:26px;height:26px;margin:0 auto;border-radius:50%;background:#eee;font-size:15px;line-height:22px}
.day small{display:block;font-size:5px;margin-top:-6px}
.day i{display:block;font-style:normal;font-size:6.5px;font-weight:700;margin-top:4px}
.news-text{font-size:6.5px;color:var(--red);line-height:8.5px}
.news-text .more{display:block;margin:3px 0 0;font-size:6.5px}
.ad{left:565px;width:153px;height:144px;background:var(--navy);color:var(--white);padding:12px 0 0 15px;line-height:1}
.ad span{display:block;font-size:19px;font-weight:700;letter-spacing:-.8px}
.ad strong{display:block;font-size:27px;font-weight:900;letter-spacing:-1px;margin-top:3px;line-height:26px}
.spinner{position:absolute;left:330px;top:1088px}
.footer{position:absolute;left:0;top:1163px;width:869px;height:37px;background:var(--blue);color:#bcd3ea;font-size:6.5px;line-height:37px}
.footer .links{position:absolute;left:145px}
.footer .copy{position:absolute;right:151px}
</style>
</head>
<body>
<header class="header">
  <div class="brand"><span class="brand-name">VINGTORGET</span></div>
  <div class="social" aria-label="Social links"><span></span><span></span><span></span><span></span></div>
</header>
<nav class="nav">
  <ul><li>Airplanes</li><li>Helicopters / Gyrocopters</li><li>Parts</li><li>Literature</li><li>Misc</li></ul>
  <div class="search">Search Parts, Copters, Airplanes......</div>
  <div class="search-btn"><svg width="14" height="14" viewBox="0 0 14 14"><circle cx="6" cy="6" r="4.3" fill="none" stroke="#fff" stroke-width="2"/><line x1="9" y1="9" x2="13" y2="13" stroke="#fff" stroke-width="2.4"/></svg></div>
</nav>

<h1 class="page-title">Aircraft For Sale - The Largest Market For Flights</h1>
<p class="welcome">Welcome Back ! Site Is Under Reconstruction / Website Is Under Reconstruction <a>Upload / Change Ad (add / Edit Your Ad)</a></p>
<div class="rule"></div>

<article class="card" style="top:248px;height:190px">
  <h2 class="card-head">Aerolite CX ULC</h2>
  <div class="thumbs">
    <div role="img" aria-label="Red aircraft propeller close-up" style="background:linear-gradient(135deg,#6b2a22,#c23b2e)"></div>
    <div role="img" aria-label="Red aircraft on water" style="background:linear-gradient(135deg,#8a9aa0,#b2463a)"></div>
    <div role="img" aria-label="Red aircraft in flight" style="background:linear-gradient(135deg,#e6e6ea,#c9c9d2)"></div>
    <div role="img" aria-label="Aircraft over mountains" style="background:linear-gradient(180deg,#d9cfc4,#8a8f98)"></div>
    <div role="img" aria-label="Aircraft at sunset" style="background:linear-gradient(135deg,#e7d4a6,#c0a26a)"></div>
  </div>
  <div class="desc">Experimental clipped wing +9 /-6G airshow performer for sale in Norway. Two stroke TwinPort T582 fully inverted system. Built in 1994, new wings in 2011. Total time 401 hours, 135 engine hours. Customized pocket fighter........ <span class="more">View More &gt;&gt;</span></div>
  <div class="meta">
    <span><svg width="10" height="10" viewBox="0 0 10 10"><path d="M5 0l1.5 3.3 3.5.4-2.6 2.4.7 3.5L5 7.8 1.9 9.6l.7-3.5L0 3.7l3.5-.4z" fill="#0a5aa8"/></svg>Aero Accessories, TT 222 hrs,</span>
    <span><svg width="10" height="10" viewBox="0 0 10 10"><rect x="1" y="2" width="8" height="6" rx="1" fill="#0a5aa8"/></svg><b>Price :</b> 1200 SEK</span>
    <span><svg width="9" height="10" viewBox="0 0 9 10"><circle cx="4.5" cy="3" r="2.5" fill="#0a5aa8"/><path d="M0 10c0-3 2-4.5 4.5-4.5S9 7 9 10z" fill="#0a5aa8"/></svg><b>Name :</b> Arne-Bo</span>
    <span><svg width="10" height="10" viewBox="0 0 10 10"><rect width="10" height="10" rx="1.5" fill="#0a5aa8"/><path d="M3 2l1.2 1.5-.7 1a4 4 0 002 2l1-.7L8 7 7 8.3C4.5 8 2 5.5 1.8 3z" fill="#fff"/></svg><b>Phone :</b> 0700-555123</span>
  </div>
  <div class="dated"><svg width="10" height="10" viewBox="0 0 10 10" style="margin-right:4px"><circle cx="5" cy="5" r="4" fill="none" stroke="#0a5aa8" stroke-width="1.4"/><path d="M5 2.5V5h2" stroke="#0a5aa8" fill="none"/></svg>Date : 2013-10-05 19:31:18<span class="dots"></span><span class="btn">Read More</span></div>
</article>

<article class="card" style="top:452px;height:142px">
  <h2 class="card-head">Aerolite CX ULC</h2>
  <div class="desc" style="padding-top:12px">Experimental clipped wing +9 /-6G airshow performer for sale in Norway. Two stroke TwinPort T582 fully inverted system. Built in 1994, new wings in 2011. Total time 401 hours, 135 engine hours. Customized pocket fighter........ <span class="more">View More &gt;&gt;</span></div>
  <div class="meta" style="margin-top:9px">
    <span><svg width="10" height="10" viewBox="0 0 10 10"><path d="M5 0l1.5 3.3 3.5.4-2.6 2.4.7 3.5L5 7.8 1.9 9.6l.7-3.5L0 3.7l3.5-.4z" fill="#0a5aa8"/></svg>Aero Accessories, TT 222 hrs,</span>
    <span><svg width="10" height="10" viewBox="0 0 10 10"><rect x="1" y="2" width="8" height="6" rx="1" fill="#0a5aa8"/></svg><b>Price :</b> 1200 SEK</span>
    <span><svg width="9" height="10" viewBox="0 0 9 10"><circle cx="4.5" cy="3" r="2.5" fill="#0a5aa8"/><path d="M0 10c0-3 2-4.5 4.5-4.5S9 7 9 10z" fill="#0a5aa8"/></svg><b>Name :</b> Arne-Bo</span>
    <span><svg width="10" height="10" viewBox="0 0 10 10"><rect width="10" height="10" rx="1.5" fill="#0a5aa8"/><path d="M3 2l1.2 1.5-.7 1a4 4 0 002 2l1-.7L8 7 7 8.3C4.5 8 2 5.5 1.8 3z" fill="#fff"/></svg><b>Phone :</b> 0700-555123</span>
  </div>
  <div class="dated"><svg width="10" height="10" viewBox="0 0 10 10" style="margin-right:4px"><circle cx="5" cy="5" r="4" fill="none" stroke="#0a5aa8" stroke-width="1.4"/><path d="M5 2.5V5h2" stroke="#0a5aa8" fill="none"/></svg>Date : 2013-10-05 19:31:18<span class="dots"></span><span class="btn">Read More</span></div>
</article>

<article class="card" style="top:608px;height:167px">
  <h2 class="card-head">Aerolite CX ULC</h2>
  <div class="side-photo">
    <div class="thumb" role="img" aria-label="Yellow aircraft on grass field" style="background:linear-gradient(180deg,#c9cfd6,#d4b43a 50%,#6e6a4a)"></div>
    <div class="desc" style="padding-left:20px">Experimental clipped wing +9 /-6G airshow performer for sale in Norway. Two stroke TwinPort T582 fully inverted system. Built in 1994, new wings in 2011. Total time 401 hours, 135 engine hours. Customized pocket fighter........<br><span class="more" style="margin:0;line-height:22px">View More &gt;&gt;</span></div>
  </div>
  <div class="meta" style="margin-top:2px">
    <span><svg width="10" height="10" viewBox="0 0 10 10"><path d="M5 0l1.5 3.3 3.5.4-2.6 2.4.7 3.5L5 7.8 1.9 9.6l.7-3.5L0 3.7l3.5-.4z" fill="#0a5aa8"/></svg>Aero Accessories, TT 222 hrs,</span>
    <span><svg width="10" height="10" viewBox="0 0 10 10"><rect x="1" y="2" width="8" height="6" rx="1" fill="#0a5aa8"/></svg><b>Price :</b> 1200 SEK</span>
    <span><svg width="9" height="10" viewBox="0 0 9 10"><circle cx="4.5" cy="3" r="2.5" fill="#0a5aa8"/><path d="M0 10c0-3 2-4.5 4.5-4.5S9 7 9 10z" fill="#0a5aa8"/></svg><b>Name :</b> Arne-Bo</span>
    <span><svg width="10" height="10" viewBox="0 0 10 10"><rect width="10" height="10" rx="1.5" fill="#0a5aa8"/><path d="M3 2l1.2 1.5-.7 1a4 4 0 002 2l1-.7L8 7 7 8.3C4.5 8 2 5.5 1.8 3z" fill="#fff"/></svg><b>Phone :</b> 0700-555123</span>
  </div>
  <div class="dated"><svg width="10" height="10" viewBox="0 0 10 10" style="margin-right:4px"><circle cx="5" cy="5" r="4" fill="none" stroke="#0a5aa8" stroke-width="1.4"/><path d="M5 2.5V5h2" stroke="#0a5aa8" fill="none"/></svg>Date : 2013-10-05 19:31:18<span class="dots"></span><span class="btn">Read More</span></div>
</article>

<article class="card" style="top:790px;height:276px">
  <h2 class="card-head">Aerolite CX ULC</h2>
  <div class="thumbs" style="padding-left:17px">
    <div role="img" aria-label="Yellow aircraft on field" style="background:linear-gradient(180deg,#cfd6dc,#c9a93a 55%,#6b6240)"></div>
    <div role="img" aria-label="Red aircraft parked" style="background:linear-gradient(135deg,#9fb08a,#c5463a)"></div>
    <div role="img" aria-label="Yellow aircraft on grass" style="background:linear-gradient(180deg,#b9c6b2,#d8c84a 55%,#7a8a5a)"></div>
    <div role="img" aria-label="Yellow aircraft on beach" style="background:linear-gradient(180deg,#9fc3de,#e0d8b0)"></div>
    <div role="img" aria-label="Aircraft instrument panel" style="background:linear-gradient(135deg,#8a8f94,#3f4449)"></div>
  </div>
  <div class="desc">
    <p>Experimental clipped wing +9 /-6G airshow performer for sale in Norway. Two stroke TwinPort T582 fully inverted system. Built in 1994, new wings in 2011. Total time 401 hours, 135 engine hours. Customized pocket fighter........</p>
    <p>Experimental clipped wing +9 /-6G airshow performer for sale in Norway. Two stroke TwinPort T582 fully inverted system. Built in 1994, new wings in 2011. Total time 401 hours, 135 engine hours. Customized pocket fighter........</p>
    <p>Experimental clipped wing +9 /-6G airshow performer for sale in Norway. Two stroke TwinPort T582 fully inverted system. Built in 1994, new wings in 2011. Total time 401 hours, 135 engine hours. Customized pocket fighter........ <span class="more">View More &gt;&gt;</span></p>
  </div>
  <div class="meta" style="margin-top:5px">
    <span><svg width="10" height="10" viewBox="0 0 10 10"><path d="M5 0l1.5 3.3 3.5.4-2.6 2.4.7 3.5L5 7.8 1.9 9.6l.7-3.5L0 3.7l3.5-.4z" fill="#0a5aa8"/></svg>Aero Accessories, TT 222 hrs,</span>
    <span><svg width="10" height="10" viewBox="0 0 10 10"><rect x="1" y="2" width="8" height="6" rx="1" fill="#0a5aa8"/></svg><b>Price :</b> 1200 SEK</span>
    <span><svg width="9" height="10" viewBox="0 0 9 10"><circle cx="4.5" cy="3" r="2.5" fill="#0a5aa8"/><path d="M0 10c0-3 2-4.5 4.5-4.5S9 7 9 10z" fill="#0a5aa8"/></svg><b>Name :</b> Arne-Bo</span>
    <span><svg width="10" height="10" viewBox="0 0 10 10"><rect width="10" height="10" rx="1.5" fill="#0a5aa8"/><path d="M3 2l1.2 1.5-.7 1a4 4 0 002 2l1-.7L8 7 7 8.3C4.5 8 2 5.5 1.8 3z" fill="#fff"/></svg><b>Phone :</b> 0700-555123</span>
  </div>
  <div class="dated"><svg width="10" height="10" viewBox="0 0 10 10" style="margin-right:4px"><circle cx="5" cy="5" r="4" fill="none" stroke="#0a5aa8" stroke-width="1.4"/><path d="M5 2.5V5h2" stroke="#0a5aa8" fill="none"/></svg>Date : 2013-10-05 19:31:18<span class="dots"></span><span class="btn">Read More</span></div>
</article>

<aside class="side video">
  <h3 class="box-head">See Our Video</h3>
  <div class="video-frame"><div role="img" aria-label="Video still of a vintage aircraft">
    <svg width="22" height="22" viewBox="0 0 22 22" style="position:absolute;left:65px;top:35px"><circle cx="11" cy="11" r="10" fill="#eee" opacity=".85"/><path d="M8.5 6.5l7 4.5-7 4.5z" fill="#222"/></svg>
    <div style="position:absolute;left:0;right:0;bottom:0;height:7px;background:#111"></div>
  </div></div>
</aside>

<aside class="side news">
  <h3 class="box-head">Latest News</h3>
  <div class="news-item"><div class="day"><b>18</b><small>AUG</small><i>5:00 PM</i></div><div class="news-text">Lorem Ipsum Dolor Sit Amet, Consectetuer Adipiscing Elit Dolor Sit Amet, Consectetuer<span class="more">View More &gt;&gt;</span></div></div>
  <div class="news-item"><div class="day"><b>17</b><small>AUG</small><i>5:00 PM</i></div><div class="news-text">Lorem Ipsum Dolor Sit Amet, Consectetuer Adipiscing Elit Dolor Sit Amet, Consectetuer<span class="more">View More &gt;&gt;</span></div></div>
  <div class="news-item"><div class="day"><b>16</b><small>AUG</small><i>5:00 PM</i></div><div class="news-text">Lorem Ipsum Dolor Sit Amet, Consectetuer Adipiscing Elit Dolor Sit Amet, Consectetuer<span class="more">View More &gt;&gt;</span></div></div>
</aside>

<aside class="side ad" style="top:593px"><span>Advertise Your</span><strong>BUSINESS<br>HERE...</strong></aside>
<aside class="side ad" style="top:748px"><span>Advertise Your</span><strong>BUSINESS<br>HERE...</strong></aside>

<svg class="spinner" width="50" height="50" viewBox="0 0 50 50" aria-label="Loading">
  <g fill="none" stroke-width="8">
    <circle cx="25" cy="25" r="20" stroke="#9a9a9a" stroke-dasharray="12 3.7"/>
  </g>
</svg>

<footer class="footer">
  <div class="links">HOME | &nbsp;SITEMAP | &nbsp;CAREERS | &nbsp;CONTACT US | PRIVACY POLICY</div>
  <div class="copy">COPYRIGHT © 2013 VINGTORGET ALL RIGHTS RESERVS</div>
</footer>
</body>
</html>
```